Thyroid treatment trifold brochure

We need a trifold brochure to have on display at other businesses, especially targeted for women ages 35 -65. Highlighting Hair loss, weight gain, lack of answers from Primary care dr. We specialize in hormone balancing with bio-identical hormone replacement. the uploaded file is an example from another clinic that has good info. I would like to also focus on how we are approach therapy different and find answers where other clinics fail. The most effective approach is the right medicine, (naturally dessicated Thyroid medication) and paying attention to symptoms. Most doctors are only trained to look at bloodwork and adjust a synthetic thyroid med. So many women are frustrated by the lack of help available.
Want thicker fuller hair? Check your thyroid!
Thinning Hair, Hairline and Eyebrows? #1 Reason and how to reverse it.
Is your thyroid medication causing hair loss?
• The truth is that levothyroxine itself can cause hair loss independent of whatever dose you are taking.
• It may be the case that you are taking the exact amount of levothyroxine that your body needs to function but you can STILL experience hair loss.
• That's because one of the side effects of levothyroxine is hair loss.
If you aren't seeing improvement in your hair growth after changing your thyroid medication to an naturally desiccated medication, then look to these nutrients:
• Selenium
• Zinc
• Iron
• Vitamin B12
• Biotin
• Choline
These nutrients are necessary for hair growth and if you don't have enough of them your hair will not grow even if your thyroid is stimulating your hair follicles.
Are your thyroid medications working? Here is how to tell
7 Thyroid medications mistakes you don’t want to make
1. You’re on the wrong medication for your body - Synthetic vs. Bio-Identical
2. You don’t take your medication correctly
3. You don’t store your medication properly
4. You don't separate coffee, milk, and your thyroid medication
5. You ignore continued symptoms that should have resolved
6. You use a Doctor that only relies on blood work to diagnose
7. You don’t know if you have glandular vs. cellular hypothyroidism

Thyroid Quiz
In the last few weeks have you:
Felt tired?
Gained Weight?
Felt colder than other people?
Had Constipation?
Had Hair problems?
Had Skin Problems?
Had Nail Problems?
Had a Loss of Appetite?
Had hearing problems?
Had voice problems?
Had speech problems?
Had memory problems?
Had problems with concentration?
Felt giddy of dizzy?
Felt depressed or low?

Yes no

Target Market(s)

women 35-65

Industry/Entity Type

medical clinic

Colors
0094D4
00A9DD
6FCCEA
C7EBF8
E9F6FB

Requirements
Nice to have
• a little quiz or tips on checking for sign's by looking in the mirror

```html
<!DOCTYPE html>
<html lang="en">
<head>
<meta charset="utf-8">
<title>Lumaleaf MD – Thyroid Trifold Brochure</title>
<link href="https://fonts.googleapis.com/css2?family=Montserrat:wght@400;500;600;700;800&display=swap" rel="stylesheet">
<style>
:root{
  --green:#93b047;
  --green-dark:#7f9c37;
  --panel-grey:#d9d9d9;
  --panel-light:#ececec;
  --paper:#f6f6f6;
  --text:#4a4a4a;
  --muted:#8c8c8c;
  --heading-grey:#a9a9a9;
  --backdrop:#e4e4e2;
  --white:#ffffff;
}
*{box-sizing:border-box;margin:0;padding:0}
html,body{width:1200px;height:900px;overflow:hidden;background:var(--backdrop);font-family:"Montserrat",sans-serif;color:var(--text)}
.stage{position:relative;width:1200px;height:900px}
.spread{position:absolute;top:245px;width:590px;height:410px;background:var(--paper);overflow:hidden;box-shadow:0 6px 18px rgba(0,0,0,.14)}
.spread--outside{left:8px}
.spread--inside{left:602px}
.abs{position:absolute}
.fold{position:absolute;top:0;width:1px;height:100%;background:rgba(0,0,0,.06)}
.placeholder-photo{position:absolute}
.brand{position:absolute;display:flex;align-items:center;gap:5px;color:var(--green);font-weight:700;white-space:nowrap}
.brand__dot{border-radius:50%;background:var(--green);flex:none}

/* outside – quiz panel */
.quiz-panel{left:0;width:193px;height:100%;background:var(--panel-light)}
.quiz-watermark{left:118px;top:16px;font-size:58px;font-weight:800;color:rgba(0,0,0,.05);letter-spacing:-1px}
.quiz-side-block{left:0;top:99px;width:90px;height:311px;background:var(--panel-grey);border-top-right-radius:22px}
.quiz-title{left:108px;top:100px;font-size:17px;font-weight:700;color:var(--green)}
.quiz-list{left:108px;top:126px;list-style:none;font-size:5.4px;line-height:9.25px;color:var(--text)}
.quiz-answer{left:108px;top:288px;font-size:6px;font-weight:700}
.quiz-band{left:9px;top:352px;width:184px;height:58px;background:var(--green);border-top-left-radius:16px}

/* outside – contact panel */
.contact-panel{left:193px;width:194px;height:100%;background:#e6e6e6}
.contact-band{left:193px;top:354px;width:194px;height:56px;background:var(--green)}
.contact-title{left:193px;width:194px;top:212px;text-align:center;font-size:16px;font-weight:700;color:var(--heading-grey)}
.contact-list{left:193px;width:194px;top:236px;text-align:center;list-style:none}
.contact-list dt{font-size:4.4px;font-weight:600;color:var(--muted);letter-spacing:.3px;margin-top:7px}
.contact-list dd{font-size:6px;font-weight:600;color:var(--green);margin-top:2px}
.social{display:flex;align-items:center;justify-content:center;gap:3px;margin-top:4px}
.social i{width:7px;height:7px;border-radius:50%;background:var(--muted);display:inline-block}

/* outside – cover panel */
.cover-panel{left:387px;width:203px;height:100%;background:#f2f2f2}
.cover-headline{left:405px;top:144px;width:120px;font-size:12.5px;line-height:16px;font-weight:800;color:var(--white)}
.cover-tag{left:402px;top:186px;width:160px;height:86px;background:var(--green);border-radius:0 28px 8px 8px;padding:34px 8px 0;text-align:center;color:var(--white);font-size:8px;line-height:10.5px;font-weight:700}
.cover-band{left:388px;top:352px;width:154px;height:58px;background:var(--green);border-top-right-radius:16px}

/* inside */
.inside-panel-a{left:0;width:198px;height:100%;background:#d6d6d6}
.inside-panel-b{left:198px;width:195px;height:100%;background:#f1f1f1}
.inside-panel-c{left:393px;width:197px;height:100%;background:#f7f7f7}
.heading-green{color:var(--green);font-weight:700}
.meds-title{left:21px;top:104px;width:150px;font-size:11.5px;line-height:13px}
.meds-intro{left:21px;top:140px;width:140px;font-size:7.6px;line-height:9.5px;font-weight:700;color:var(--muted);text-align:justify}
.mistakes{left:21px;top:188px;width:150px;list-style:none;font-size:5.2px;line-height:8px}
.mistakes li{display:flex;gap:4px;margin-bottom:.5px}
.mistakes b{color:var(--muted);font-size:7px;width:5px;flex:none}
.web-tab{left:3px;top:386px;width:160px;height:28px;background:#bdbdbd;border-top-right-radius:12px;color:var(--white);font-size:12px;font-weight:500;padding:6px 0 0 24px}
.hair-arc{left:121px;top:236px;width:275px;height:190px;border-top-left-radius:160px;background:var(--green)}
.hair-arc__photo{left:133px;top:248px;width:263px;height:170px;border-top-left-radius:150px;background:linear-gradient(135deg,#8f8a86,#4d4542 60%,#9a9592)}
.nutrients-title{left:228px;top:40px;width:140px;font-size:10.5px;line-height:12px}
.nutrients{left:236px;top:140px;list-style:none;font-size:5.6px;line-height:7.3px}
.nutrients li::before{content:"·";margin-right:14px}
.nutrients-note{left:228px;top:192px;width:136px;font-size:6px;line-height:7.6px;font-weight:700;color:var(--muted);text-align:justify}
.loss-photo{left:426px;top:90px;width:126px;height:122px;border-radius:12px;background:linear-gradient(160deg,#6f7a6a,#3e3a38 55%,#7b8fa6)}
.loss-title{left:416px;top:222px;width:140px;font-size:12px;line-height:14px}
.loss-list{left:416px;top:266px;width:160px;list-style:none;font-size:5.2px;line-height:6.4px}
.loss-list li{display:flex;gap:8px;margin-bottom:7px;text-align:justify}
.loss-list li::before{content:"•";flex:none}
.brand-small{left:456px;top:380px}
.brand-url{left:456px;top:394px;font-size:4px;color:var(--green);font-weight:600}
</style>
</head>
<body>
<main class="stage">

  <!-- Outside of the trifold -->
  <section class="spread spread--outside" aria-label="Brochure outside">
    <div class="abs quiz-panel"></div>
    <div class="abs contact-panel"></div>
    <div class="abs cover-panel"></div>

    <div class="abs quiz-watermark" aria-hidden="true">Quiz</div>
    <div class="abs quiz-side-block"></div>
    <div class="placeholder-photo" role="img" aria-label="Small illustration of two people beside yes and no bubbles" style="left:21px;top:54px;width:70px;height:40px;background:linear-gradient(90deg,#c9d6a8,#dfe6cf);border-radius:6px"></div>
    <h2 class="abs quiz-title">Thyroid Quiz</h2>
    <ul class="abs quiz-list">
      <li>In the last few weeks have you:</li>
      <li>Felt tired?</li>
      <li>Gained Weight?</li>
      <li>Felt colder than other people?</li>
      <li>Had Constipation?</li>
      <li>Had Hair problems?</li>
      <li>Had Skin Problems?</li>
      <li>Had Nail Problems?</li>
      <li>Had a Loss of Appetite?</li>
      <li>Had hearing problems?</li>
      <li>Had voice problems?</li>
      <li>Had speech problems?</li>
      <li>Had memory problems?</li>
      <li>Had problems with concentration?</li>
      <li>Felt giddy of dizzy?</li>
      <li>Felt depressed or low?</li>
    </ul>
    <div class="abs quiz-answer">Yes / No</div>
    <div class="abs quiz-band"></div>
    <div class="placeholder-photo" role="img" aria-label="Illustration of a puzzled woman shrugging among question marks and yes/no bubbles" style="left:24px;top:290px;width:120px;height:120px;background:linear-gradient(180deg,#e4e4e4,#e7a08e 70%,#d98876);border-radius:10px 10px 0 0"></div>

    <div class="placeholder-photo" role="img" aria-label="Photo of long wavy hair styled with small flower pins" style="left:303px;top:0;width:210px;height:198px;background:linear-gradient(120deg,#cfc9c4,#a58a72 50%,#d9d3cd);border-bottom-left-radius:22px"></div>
    <h2 class="abs contact-title">Contact Us</h2>
    <dl class="abs contact-list">
      <dt>PHONE NUMBERS</dt><dd>+1 1234 1234 / 1234</dd>
      <dt>WEBSITE</dt><dd>www.your web.com</dd>
      <dt>ADDRESS</dt><dd>YOUR ADDRESS HERE</dd>
      <dt>SOCIAL MEDIA</dt>
      <dd class="social"><i></i>social.example/lumaleaf</dd>
      <dd class="social"><i></i>photos.example/lumaleaf</dd>
      <dd class="social"><i></i>posts.example/lumaleaf</dd>
    </dl>
    <div class="abs contact-band"></div>

    <div class="abs cover-tag">Thinning Hair, Hairline and Eyebrows? #1 Reason and how to reverse it.</div>
    <div class="placeholder-photo" role="img" aria-label="Circular photo of a woman's braided auburn hair seen from behind" style="left:409px;top:50px;width:140px;height:140px;border-radius:50%;background:radial-gradient(circle at 55% 40%,#b57a4e,#8f6246 55%,#d8cfc8)"></div>
    <h1 class="abs cover-headline">Want thicker fuller hair? Check your thyroid!</h1>
    <div class="brand" style="left:440px;top:300px;font-size:19px"><span class="brand__dot" style="width:12px;height:12px"></span>Lumaleaf MD</div>
    <div class="abs cover-band"></div>

    <div class="fold" style="left:193px"></div>
    <div class="fold" style="left:387px"></div>
  </section>

  <!-- Inside of the trifold -->
  <section class="spread spread--inside" aria-label="Brochure inside">
    <div class="abs inside-panel-a"></div>
    <div class="abs inside-panel-b"></div>
    <div class="abs inside-panel-c"></div>

    <div class="brand" style="left:21px;top:64px;font-size:17px"><span class="brand__dot" style="width:11px;height:11px"></span>Lumaleaf MD</div>
    <h2 class="abs heading-green meds-title">Are your thyroid medications working?</h2>
    <p class="abs meds-intro">Are your thyroid medications working? Here is how to tell 7 Thyroid medications mistakes you don't want to make</p>
    <ol class="abs mistakes">
      <li><b>1</b><span>You're on the wrong medication for your body - Synthetic vs. Bio-Identical</span></li>
      <li><b>2</b><span>You don't take your medication correctly</span></li>
      <li><b>3</b><span>You don't store your medication properly</span></li>
      <li><b>4</b><span>You don't separate coffee, milk, and your thyroid medication</span></li>
      <li><b>5</b><span>You ignore continued symptoms that should have resolved</span></li>
      <li><b>6</b><span>You use a Doctor that only relies on blood work to diagnose</span></li>
      <li><b>7</b><span>You don't know if you have glandular vs. cellular hypothyroidism</span></li>
    </ol>
    <div class="abs hair-arc"></div>
    <div class="abs hair-arc__photo" role="img" aria-label="Photo of a woman tossing long dark hair"></div>
    <div class="abs web-tab">lumaleafmd.com</div>

    <h2 class="abs heading-green nutrients-title">If you aren't seeing improvement in your hair growth after changing your thyroid medication to an naturally desiccated medication, then look to these nutrients:</h2>
    <ul class="abs nutrients">
      <li>Selenium</li><li>Zinc</li><li>Iron</li><li>Vitamin B12</li><li>Biotin</li><li>Choline</li>
    </ul>
    <p class="abs nutrients-note">These nutrients are necessary for hair growth and if you don't have enough of them your hair will not grow even if your thyroid is stimulating your hair follicles.</p>

    <div class="abs loss-photo" role="img" aria-label="Photo of a woman with long flowing hair in a denim jacket outdoors"></div>
    <h2 class="abs heading-green loss-title">Is your thyroid medication causing hair loss?</h2>
    <ul class="abs loss-list">
      <li>The truth is that levothyroxine itself can cause hair loss independent of whatever dose you are taking.</li>
      <li>It may be the case that you are taking the exact amount of levothyroxine that your body needs to function but you can STILL experience hair loss.</li>
      <li>That's because one of the side effects of levothyroxine is hair loss.</li>
    </ul>
    <div class="brand brand-small" style="font-size:9px"><span class="brand__dot" style="width:6px;height:6px"></span>Lumaleaf MD</div>
    <div class="abs brand-url">lumaleafmd.com</div>

    <div class="fold" style="left:198px"></div>
    <div class="fold" style="left:393px"></div>
  </section>

</main>
</body>
</html>
```